Pemberton Dialworks Business Card Design

Double Sided Business Card Design for a Locksmith company specializing in Safecracking, safe & vault service.

```html
<!DOCTYPE html>
<html lang="en">
<head>
<meta charset="UTF-8">
<title>Pemberton Dialworks Business Card</title>
<link href="https://fonts.googleapis.com/css2?family=Open+Sans:wght@400;700;800&display=swap" rel="stylesheet">
<style>
  :root {
    --backdrop: #1b1b1b;
    --card: #f4f4f4;
    --card-shade: #e6e6e6;
    --brand-green: #2f7d34;
    --ink: #1a1a1a;
    --muted: #555555;
    --divider: rgba(0,0,0,0.12);
  }
  * { box-sizing: border-box; margin: 0; padding: 0; }
  html, body {
    width: 1200px; height: 900px; overflow: hidden;
    background: var(--backdrop);
    font-family: "Open Sans", sans-serif;
  }
  .canvas {
    position: relative; width: 1200px; height: 900px;
    display: flex; flex-direction: column; align-items: center; justify-content: center; gap: 50px;
  }
  .card {
    position: relative; width: 560px; height: 320px;
    background: linear-gradient(135deg, var(--card) 0%, #ffffff 50%, var(--card-shade) 100%);
    border-radius: 22px;
    box-shadow: 0 18px 40px rgba(0,0,0,0.55);
    overflow: hidden;
  }
  .brand {
    display: flex; align-items: center; gap: 16px;
  }
  .brand-dot {
    flex: none; border-radius: 50%; background: var(--brand-green);
  }
  .brand-name {
    font-weight: 800; color: var(--brand-green);
    text-transform: uppercase; line-height: 1.02; letter-spacing: 0.5px;
  }
  /* Front */
  .card-front { display: flex; align-items: center; justify-content: center; }
  .card-front .brand-dot { width: 78px; height: 78px; }
  .card-front .brand-name { font-size: 38px; }
  /* Back */
  .card-back .brand { position: absolute; left: 40px; top: 70px; }
  .card-back .brand-dot { width: 52px; height: 52px; }
  .card-back .brand-name { font-size: 24px; }
  .card-back .fold {
    position: absolute; left: 250px; top: 150px; width: 2px; height: 190px;
    background: linear-gradient(to bottom, transparent, var(--divider), transparent);
    transform: rotate(38deg); transform-origin: top;
  }
  .contact {
    position: absolute; left: 300px; top: 150px;
  }
  .contact-name {
    font-weight: 700; font-size: 17px; color: var(--brand-green);
    text-transform: uppercase; letter-spacing: 0.4px;
  }
  .contact-role { font-size: 14px; color: var(--muted); margin-bottom: 16px; }
  .contact-line {
    display: flex; align-items: center; gap: 8px;
    font-size: 13.5px; color: var(--muted); line-height: 1.55;
  }
  .contact-line svg { width: 12px; height: 12px; fill: var(--brand-green); flex: none; }
  .contact-line.web { color: var(--brand-green); }
</style>
</head>
<body>
<main class="canvas">
  <section class="card card-front">
    <div class="brand">
      <span class="brand-dot"></span>
      <span class="brand-name">Pemberton<br>Dialworks</span>
    </div>
  </section>

  <section class="card card-back">
    <div class="brand">
      <span class="brand-dot"></span>
      <span class="brand-name">Pemberton<br>Dialworks</span>
    </div>
    <div class="fold"></div>
    <div class="contact">
      <p class="contact-name">Nolan R. Whitfield</p>
      <p class="contact-role">Co-Founder &amp; Partner</p>
      <p class="contact-line">
        <svg viewBox="0 0 24 24"><path d="M6.6 10.8a15 15 0 0 0 6.6 6.6l2.2-2.2a1 1 0 0 1 1-.25 11.4 11.4 0 0 0 3.6.57 1 1 0 0 1 1 1V20a1 1 0 0 1-1 1A17 17 0 0 1 3 4a1 1 0 0 1 1-1h3.5a1 1 0 0 1 1 1c0 1.25.2 2.45.57 3.57a1 1 0 0 1-.25 1z"/></svg>
        (214) 555-0148
      </p>
      <p class="contact-line">
        <svg viewBox="0 0 24 24"><path d="M2 5h20v14H2z M2 5l10 8 10-8" fill="none" stroke="#2f7d34" stroke-width="2.4"/></svg>
        Nolan@pembertondialworks.com
      </p>
      <p class="contact-line web">
        <svg viewBox="0 0 24 24"><circle cx="12" cy="12" r="10" fill="none" stroke="#2f7d34" stroke-width="2.4"/><path d="M2 12h20M12 2c3 3 3 17 0 20M12 2c-3 3-3 17 0 20" fill="none" stroke="#2f7d34" stroke-width="2"/></svg>
        pembertondialworks.com
      </p>
    </div>
  </section>
</main>
</body>
</html>
```